Business Card Design for New Game Studio

We need a business card design. We are a new company developing innovative mobile and platform games.

I would like to see very innovative design thats brings out the company's goal and direction.

My Company's goal and direction is to "Evolve the way of gaming, Bring fun and entertainment to all gamers"

Please do use our company logo which I have attached to be included in the design.

Please put in details for name, title, contacts etc ... be creative !!!

Reason: Company logo redesign. Awaiting it. Thanks

Hi all Please do wait for my updated company logo. Thanks

Reason: Still waiting on new company logo. Thanks all

Hi All Designers .... Sorry for the long wait... Please see the new file for my new company logo uploaded. Waiting to see all your creative design. Cheers

Hi All .... Please do not just mass send a whole bunch of similar designs .... Would like to see quality instead of quantity Cheers

Entertainment

```html
<!DOCTYPE html>
<html lang="en">
<head>
<meta charset="utf-8">
<title>Nova Quest – Business Card</title>
<link rel="stylesheet" href="https://fonts.googleapis.com/css2?family=Questrial&display=swap">
<style>
  :root {
    --backdrop: #e7e3dd;
    --lime: #a2dd44;
    --lime-deep: #8fcb34;
    --charcoal: #26292c;
    --ink: #1d2225;
    --teal: #2b6775;
    --teal-band: #21505b;
    --contact-text: #d9dde0;
  }
  * { margin: 0; padding: 0; box-sizing: border-box; }
  html, body {
    width: 1200px; height: 1001px; overflow: hidden;
    background: var(--backdrop);
    font-family: "Questrial", "Century Gothic", sans-serif;
  }
  .card {
    position: absolute; left: 393px; width: 512px; height: 290px;
    overflow: hidden;
    box-shadow: 0 6px 14px rgba(0,0,0,.25);
  }
  .card--front { top: 171px; background: var(--lime); }
  .card--back { top: 538px; background: var(--charcoal); }

  .brand {
    display: flex; align-items: center; gap: 10px;
    color: var(--ink); font-size: 34px; white-space: nowrap;
  }
  .brand__dot {
    width: 30px; height: 30px; border-radius: 50%;
    background: var(--teal); flex: none;
  }
  .card--front .brand {
    position: absolute; left: 50%; top: 78px; transform: translateX(-50%);
  }
  .front__silhouette {
    position: absolute; left: 0; bottom: 0; width: 100%; height: 60px;
    background: linear-gradient(var(--teal-band), var(--charcoal) 40%);
  }
  .front__web {
    position: absolute; left: 0; right: 0; bottom: 10px;
    text-align: center; color: var(--lime);
    font-size: 11px; letter-spacing: 4px; text-transform: uppercase;
  }

  .back__panel {
    position: absolute; left: 0; top: 0; width: 209px; height: 254px;
    background: var(--lime);
  }
  .card--back .brand {
    position: absolute; left: 50%; top: 136px; transform: translateX(-50%);
    font-size: 20px; gap: 7px;
  }
  .card--back .brand__dot { width: 20px; height: 20px; }

  .contacts {
    position: absolute; left: 252px; top: 114px; list-style: none;
    color: var(--contact-text); font-size: 12px; line-height: 16px;
  }
  .contacts li { display: flex; align-items: center; gap: 7px; }
  .contacts svg { width: 10px; height: 10px; flex: none; }

  .back__band {
    position: absolute; left: 0; bottom: 0; width: 100%; height: 36px;
    background: var(--teal-band);
  }
  .back__icons {
    position: absolute; left: 10px; right: 10px; top: 9px; height: 18px;
    background: linear-gradient(90deg, var(--lime-deep), var(--lime), var(--lime-deep));
    opacity: .55; border-radius: 3px;
  }
</style>
</head>
<body>

<section class="card card--front">
  <div class="brand"><span class="brand__dot"></span><span class="brand__name">Nova Quest</span></div>
  <div class="front__silhouette" role="img" aria-label="Jagged dark grass silhouette along the bottom edge"></div>
  <p class="front__web">www.novaquestgames.com</p>
</section>

<section class="card card--back">
  <div class="back__panel">
    <div class="brand"><span class="brand__dot"></span><span class="brand__name">Nova Quest</span></div>
  </div>

  <ul class="contacts">
    <li>
      <svg viewBox="0 0 10 10"><path d="M2 1l2 2-1 1.3c.6 1.2 1.5 2.1 2.7 2.7L7 6l2 2-1.3 1.5C4.5 9.2.8 5.5.5 2.3z" fill="var(--lime)"/></svg>
      <span>+61400123987</span>
    </li>
    <li>
      <svg viewBox="0 0 10 10"><rect x="0.5" y="2" width="9" height="6" fill="none" stroke="var(--lime)"/><path d="M.5 2l4.5 3.5L9.5 2" fill="none" stroke="var(--lime)"/></svg>
      <span>hello@novaquestgames.com</span>
    </li>
    <li>
      <svg viewBox="0 0 10 10"><circle cx="5" cy="5" r="4.3" fill="none" stroke="var(--lime)"/><path d="M.7 5h8.6M5 .7c-2.2 2.6-2.2 6 0 8.6M5 .7c2.2 2.6 2.2 6 0 8.6" fill="none" stroke="var(--lime)" stroke-width=".8"/></svg>
      <span>www.novaquestgames.com</span>
    </li>
    <li>
      <svg viewBox="0 0 10 10"><path d="M5 9.6C2.5 6.6 1.6 5 1.6 3.6a3.4 3.4 0 016.8 0C8.4 5 7.5 6.6 5 9.6z" fill="var(--lime)"/><circle cx="5" cy="3.6" r="1.2" fill="var(--charcoal)"/></svg>
      <span>PO Box 120, Elm Ridge, Vic, 3000</span>
    </li>
  </ul>

  <div class="back__band">
    <div class="back__icons" role="img" aria-label="Row of small gaming console and controller icons"></div>
  </div>
</section>

</body>
</html>
```